Shopify Design for a Homeopathic Shop

The design should let the user give a feeling of luxury and naturality(earthy).

We want to build up a alternative medicine luxury brand. The user should have a feeling of trust when visiting our shop. We stand for natural remedies.

Target Market(s)

Alternative / Left

Industry/Entity Type

Alternative Medicine

Font styles to use
Sans Serif

Colors

Designer to choose colors to be used in the design.

```html
<!DOCTYPE html>
<html lang="en">
<head>
<meta charset="utf-8">
<title>Verdura — Homeopathic Remedies</title>
<link href="https://fonts.googleapis.com/css2?family=Alice&family=Hind:wght@400;500;600&display=swap" rel="stylesheet">
<style>
:root{
  --green-dark:#2a7a2e;
  --green:#5aa832;
  --green-light:#8cc63f;
  --ink:#1c1c1c;
  --text:#3a3a3a;
  --muted:#6b6b6b;
  --line:#e2e2e2;
  --bar:#ededed;
  --soft:#f6f4f4;
  --footer:#242424;
  --footer-bottom:#111;
}
*{box-sizing:border-box;margin:0;padding:0}
html,body{width:1200px;height:2910px;overflow:hidden;background:#fff}
body{font-family:"Hind",sans-serif;color:var(--text);position:relative}
.serif{font-family:"Alice",serif}
.abs{position:absolute}

/* header */
.site-header{position:absolute;top:0;left:0;width:1200px;height:110px;border-bottom:1px solid var(--line)}
.social{position:absolute;left:132px;top:35px;display:flex;gap:8px}
.social span{width:27px;height:27px;border-radius:50%;background:#c9c9c9;display:block}
.brand{position:absolute;left:0;width:1200px;top:34px;text-align:center;font-family:"Alice",serif;font-size:34px;letter-spacing:2px;color:var(--green-dark)}
.brand small{display:block;font-size:9px;letter-spacing:6px;color:var(--text);margin-top:-4px}
.cart{position:absolute;left:1042px;top:37px}
.main-nav{position:absolute;top:110px;left:0;width:1200px;height:37px;display:flex;justify-content:center;gap:0;font-weight:600;font-size:14px;color:var(--ink);letter-spacing:.3px}
.main-nav a{display:block;padding:0 16px;line-height:26px;color:inherit;text-decoration:none}
.main-nav a:nth-child(1){margin-left:-10px}
.main-nav a+a{margin-left:22px}
.promo-bar{position:absolute;top:147px;left:0;width:1200px;height:65px;background:var(--bar);display:flex;box-shadow:0 2px 3px rgba(0,0,0,.08)}
.promo{flex:1;text-align:center;padding-top:14px;border-right:1px solid #d2d2d2}
.promo:last-child{border-right:0}
.promo b{display:block;font-family:"Alice",serif;font-weight:400;font-size:16px;color:var(--ink)}
.promo span{font-size:12px;color:var(--muted)}

/* buttons */
.btn{display:inline-block;width:183px;height:44px;line-height:46px;text-align:center;color:#fff;font-family:"Alice",serif;font-size:15px;letter-spacing:.5px;background:linear-gradient(90deg,var(--green-dark),var(--green) 60%,var(--green-light));border-radius:40px 6px 40px 6px;box-shadow:-3px 3px 0 #dfe9d5}

/* hero */
.hero{position:absolute;top:212px;left:0;width:1200px;height:402px}
.hero-photo{position:absolute;inset:0;background:linear-gradient(100deg,#f2f0ee 0%,#e8e4df 35%,#7fa060 55%,#4f7a35 70%,#6e8a4a 85%,#d9cdb8 100%)}
.hero-copy{position:absolute;left:132px;top:118px}
.hero-copy h1{font-family:"Alice",serif;font-weight:400;font-size:35px;line-height:39px;color:var(--ink)}
.hero-copy p{font-size:12.5px;line-height:15px;color:var(--ink);margin:16px 0 20px;width:320px}

/* arrivals */
.section-title{position:absolute;left:0;width:1200px;text-align:center;font-family:"Alice",serif;font-size:25px;color:var(--ink);letter-spacing:.5px}
.product{position:absolute;top:735px;width:215px}
.product .shot{height:237px;margin:0 25px 0 30px;border-radius:8px;background:radial-gradient(ellipse at center,#e8c96a 0%,#f3e7c0 40%,#fff 72%)}
.product h3{font-family:"Alice",serif;font-weight:400;font-size:17px;color:var(--ink);margin-top:41px}
.product p{font-size:12px;line-height:15px;color:var(--text);margin-top:12px}
.product .price{font-family:"Alice",serif;font-size:25px;color:var(--green-dark);margin:8px 0 0 62px}
.product .btn{margin:14px 0 0 5px}

/* about */
.about{position:absolute;top:1224px;left:0;width:1200px;height:392px;background:var(--soft)}
.about h2{position:absolute;left:134px;top:68px;font-family:"Alice",serif;font-weight:400;font-size:25px;color:var(--ink)}
.about .lead{position:absolute;left:132px;top:126px;width:440px;font-size:12.5px;line-height:15.3px;color:var(--ink)}
.about .more{position:absolute;left:134px;top:225px;width:440px;font-size:12px;line-height:15px;color:var(--muted)}
.about .btn{position:absolute;left:136px;top:296px}
.about-art{position:absolute;left:540px;top:1237px;width:660px;height:418px;border-radius:50% 40% 45% 50%;background:radial-gradient(ellipse at 60% 60%,#e8a55a 0%,#d99a55 25%,#6ea542 50%,rgba(246,244,244,0) 72%)}

/* blogs */
.blogs-sub{position:absolute;left:0;width:1200px;top:1722px;text-align:center;font-size:12.5px;line-height:15px;color:var(--ink)}
.blog{position:absolute;top:1789px;width:291px;height:394px;background:#fff;box-shadow:0 2px 8px rgba(0,0,0,.12)}
.blog .shot{height:184px}
.blog .badge{position:absolute;left:113px;top:151px;width:64px;height:64px;border-radius:50%;background:var(--green-light);border:4px solid #fff;display:flex;align-items:center;justify-content:center}
.blog h3{text-align:center;font-family:"Alice",serif;font-weight:400;font-size:21px;color:#333;margin-top:44px}
.blog p{font-size:12px;line-height:15px;color:var(--muted);margin:21px 25px 0;text-align:justify}
.blog .meta{display:flex;align-items:center;margin:21px 25px 0;font-size:14px;color:#444}
.blog .meta .date{font-family:"Alice",serif;font-size:15px;margin-left:8px;flex:1}
.blog .meta .read{font-size:13px;color:#555}
.dots{position:absolute;top:2225px;left:563px;display:flex;gap:10px}
.dots i{width:9px;height:9px;border-radius:50%;background:#c8c8c8;display:block}
.dots i:first-child{background:var(--green-light)}

/* faq */
.faq{position:absolute;top:2283px;left:0;width:1200px;height:378px;background:#f7f7f7}
.faq-leaves{position:absolute;left:0;top:0;width:440px;height:378px;background:radial-gradient(ellipse at 40% 50%,rgba(120,180,70,.35) 0%,rgba(247,247,247,0) 70%)}
.faq h2{position:absolute;left:483px;top:57px;font-family:"Alice",serif;font-weight:400;font-size:25px;color:var(--ink);letter-spacing:.5px}
.q{position:absolute;left:484px;width:584px;height:43px;border:1px solid #ddd;background:#fff;font-family:"Alice",serif;font-size:13px;color:#444;line-height:43px;padding-left:19px}
.q svg{position:absolute;right:14px;top:11px}
.answer{position:absolute;left:504px;top:176px;width:520px;font-size:12px;line-height:15px;color:var(--ink)}

/* footer */
.site-footer{position:absolute;top:2661px;left:0;width:1200px;height:209px;background:var(--footer);color:#fff}
.site-footer h4{font-family:"Alice",serif;font-weight:400;font-size:21px;position:absolute;top:48px}
.site-footer p{position:absolute;top:84px;font-size:12px;line-height:15.5px;color:#eee}
.links{position:absolute;top:88px;font-size:12.5px;line-height:24px;color:#eee;list-style:none}
.bottom-bar{position:absolute;top:2870px;left:0;width:1200px;height:40px;background:var(--footer-bottom);color:#ddd;font-size:11px}
.bottom-bar span{position:absolute;left:132px;top:13px}
.cards{position:absolute;right:132px;top:11px;display:flex;gap:7px}
.cards i{display:block;width:32px;height:20px;border-radius:3px;background:#fff}
</style>
</head>
<body>

<header class="site-header">
  <div class="social" aria-label="Social links"><span></span><span></span><span></span><span></span><span></span><span></span></div>
  <div class="brand">VERDURA<small>HOMEOPATHIC REMEDIES</small></div>
  <svg class="cart" width="26" height="24" viewBox="0 0 26 24" aria-label="Cart"><path d="M1 2h4l3 14h14l3-10H7" fill="none" stroke="#4a62b0" stroke-width="2"/><circle cx="10" cy="20" r="2" fill="#4a62b0"/><circle cx="20" cy="20" r="2" fill="#4a62b0"/></svg>
</header>

<nav class="main-nav"><a>HOME</a><a>SHOP</a><a>ABOUT</a><a>BLOG</a><a>FAQS</a><a>CONTACT</a></nav>

<div class="promo-bar">
  <div class="promo"><b>Free Delivery WorldWide</b><span>Click here for more information</span></div>
  <div class="promo"><b>Final Clearence Sale</b><span>Upto 30% Off</span></div>
  <div class="promo"><b>New Store Opening</b><span>Hey San Luis Obispo!</span></div>
</div>

<section class="hero">
  <div class="hero-photo" role="img" aria-label="Fresh rosemary and oregano sprigs with peppercorns on a rustic table"></div>
  <div class="hero-copy">
    <h1>A BALANCED<br>APPROACH TO HEALTH.</h1>
    <p>Lorem ipsum dolor sit amet, nec morbi aliquam inceptos nulla fringilla, sem ullamcorper.</p>
    <a class="btn">SHOP NOW</a>
  </div>
</section>

<h2 class="section-title" style="top:660px">NEW ARRIVALS</h2>

<div class="product" style="left:132px"><div class="shot" role="img" aria-label="Massage oil bottle"></div><h3>Lorem ipsum dolor sit</h3><p>nec morbi aliquam inceptos nulla frin-gilla, sem ullamcorper aut non mauris</p><div class="price">$ 4.23</div><a class="btn">ADD TO CART</a></div>
<div class="product" style="left:364px"><div class="shot" role="img" aria-label="Flower remedy dropper bottle and box"></div><h3>Lorem ipsum dolor sit</h3><p>nec morbi aliquam inceptos nulla frin-gilla, sem ullamcorper aut non mauris</p><div class="price">$ 6.56</div><a class="btn">ADD TO CART</a></div>
<div class="product" style="left:600px"><div class="shot" role="img" aria-label="Arnica dropper bottle"></div><h3>Lorem ipsum dolor sit</h3><p>nec morbi aliquam inceptos nulla frin-gilla, sem ullamcorper aut non mauris</p><div class="price">$ 5.69</div><a class="btn">ADD TO CART</a></div>
<div class="product" style="left:845px"><div class="shot" role="img" aria-label="Sleep spray bottle and box"></div><h3>Lorem ipsum dolor sit</h3><p>nec morbi aliquam inceptos nulla frin-gilla, sem ullamcorper aut non mauris</p><div class="price">$ 8.24</div><a class="btn">ADD TO CART</a></div>

<section class="about">
  <h2>ABOUT US</h2>
  <p class="lead">Lorem ipsum dolor sit amet, nec morbi aliquam inceptos nulla fringilla, sem ullam-corper aut non mauris, ipsum nec libero sagittis nunc eros curabitur. Tincidunt nibh repudiandae a tincidunt consectetuer adipiscing, sint praesent libero eu pel-lentesque vivamus adipiscing, lacus ultrices id, tincidunt duis. Ultricies nec dic-tumst, sed nec volutpat, quam enim, ultrices donec risus risus odio, imperdiet feugiat vitae leo tellus lectus. Ligula in amet vulputate.</p>
  <p class="more">nteger ligula justo fermentum augue rutrum curabitur, conubia mollis a semper cras vitae, est nunc nunc tortor lacus sit, et cillum, tellus sit in ornare mi. Blandit phasellus pellentesque pretium, sed libero in sed.</p>
  <a class="btn">READ MORE</a>
</section>
<div class="about-art" role="img" aria-label="Wooden mortar and pestle surrounded by chamomile, herbs and wildflowers"></div>

<h2 class="section-title" style="top:1670px">BLOGS</h2>
<p class="blogs-sub">Lorem ipsum dolor sit amet, nec morbi aliquam inceptos nulla fringilla, sem ullamcorper aut non<br>mauris, ipsum nec libero sagittis nunc eros curabitur.</p>

<article class="blog" style="left:132px">
  <div class="shot" role="img" aria-label="Essential oil bottles with lavender and lemon" style="background:linear-gradient(120deg,#f4d27a,#f7f2e6 35%,#8a3e1c 55%,#6f7fd0 80%,#f3e0a0)"></div>
  <div class="badge"><svg width="30" height="30" viewBox="0 0 30 30" fill="none" stroke="#fff" stroke-width="2"><path d="M4 15h22a11 9 0 0 1-22 0zM10 26h10M18 13l8-9"/></svg></div>
  <h3>Lorem ipsum dolor</h3>
  <p>Lorem ipsum dolor sit amet, consectetur adipiscing elit, sed do eiusmod tempor ipsum nec libero sagittis nunc eros curab.</p>
  <div class="meta"><svg width="24" height="22" viewBox="0 0 24 22" fill="none" stroke="#666" stroke-width="1.6"><rect x="1" y="3" width="22" height="18"/><path d="M1 8h22M6 1v4M18 1v4"/></svg><span class="date">15,Feb, 2019</span><span class="read">Read More →</span></div>
</article>
<article class="blog" style="left:455px">
  <div class="shot" role="img" aria-label="Amber oil bottles among clover and yellow flowers" style="background:linear-gradient(120deg,#b5a2c8,#7a4a1e 40%,#d8b73a 65%,#c686a6)"></div>
  <div class="badge"><svg width="30" height="30" viewBox="0 0 30 30" fill="none" stroke="#fff" stroke-width="2"><path d="M4 15h22a11 9 0 0 1-22 0zM10 26h10M18 13l8-9"/></svg></div>
  <h3>Lorem ipsum dolor</h3>
  <p>Lorem ipsum dolor sit amet, consectetur adipiscing elit, sed do eiusmod tempor ipsum nec libero sagittis nunc eros curab.</p>
  <div class="meta"><svg width="24" height="22" viewBox="0 0 24 22" fill="none" stroke="#666" stroke-width="1.6"><rect x="1" y="3" width="22" height="18"/><path d="M1 8h22M6 1v4M18 1v4"/></svg><span class="date">21,March, 2018</span><span class="read">Read More →</span></div>
</article>
<article class="blog" style="left:779px">
  <div class="shot" role="img" aria-label="Wooden spoon with green citrus and oil bottles" style="background:linear-gradient(120deg,#e3c1a3,#8a4026 35%,#5e8f3a 60%,#e7c8ac)"></div>
  <div class="badge"><svg width="30" height="30" viewBox="0 0 30 30" fill="none" stroke="#fff" stroke-width="2"><path d="M4 15h22a11 9 0 0 1-22 0zM10 26h10M18 13l8-9"/></svg></div>
  <h3>Lorem ipsum dolor</h3>
  <p>Lorem ipsum dolor sit amet, consectetur adipiscing elit, sed do eiusmod tempor ipsum nec libero sagittis nunc eros curab.</p>
  <div class="meta"><svg width="24" height="22" viewBox="0 0 24 22" fill="none" stroke="#666" stroke-width="1.6"><rect x="1" y="3" width="22" height="18"/><path d="M1 8h22M6 1v4M18 1v4"/></svg><span class="date">09,Jan 2019</span><span class="read">Read More →</span></div>
</article>
<div class="dots"><i></i><i></i><i></i><i></i></div>

<section class="faq">
  <div class="faq-leaves" role="img" aria-label="Scattered green leaves"></div>
  <h2>FREQUENTLY ASKED QUESTIONS</h2>
  <div class="q" style="top:109px">Lorem ipsum dolor sit amet, nec morbi aliquam inceptos nulla fringilla, sem?<svg width="21" height="21" viewBox="0 0 21 21" fill="none" stroke="#333" stroke-width="1.5"><circle cx="10.5" cy="10.5" r="9"/><path d="M6 10.5h9"/></svg></div>
  <p class="answer">Lorem ipsum dolor sit amet, nec morbi aliquam inceptos nulla fringilla, sem ullamcorper aut non mauris, ipsum nec libero sagittis nunc eros curabitur.</p>
  <div class="q" style="top:211px">Lorem ipsum dolor sit amet, nec morbi aliquam inceptos nulla fringilla, sem?<svg width="21" height="21" viewBox="0 0 21 21" fill="none" stroke="#333" stroke-width="1.5"><circle cx="10.5" cy="10.5" r="9"/><path d="M6 10.5h9M10.5 6v9"/></svg></div>
  <div class="q" style="top:265px">Lorem ipsum dolor sit amet, nec morbi aliquam inceptos nulla fringilla, sem?<svg width="21" height="21" viewBox="0 0 21 21" fill="none" stroke="#333" stroke-width="1.5"><circle cx="10.5" cy="10.5" r="9"/><path d="M6 10.5h9M10.5 6v9"/></svg></div>
</section>

<footer class="site-footer">
  <h4 style="left:132px">CONTACT US</h4>
  <p style="left:132px;width:275px">Lorem ipsum dolor sit amet, nec morbi aliquam inceptos nulla fringilla, sem ullamcorper aut non mauris, ipsum nec .</p>
  <h4 style="left:450px">WHAT’S NEW</h4>
  <p style="left:451px;width:268px">Lorem ipsum dolor sit amet, nec morbi aliquam inceptos nulla fringilla, sem ullamcorper aut non mauris, ipsum nec libero sagittis nunc eros cura-bitur. Tincidunt nibh repudiandae a tincidunt consectetuer adipiscing, sint praesent libero eu pellentesque vivamus adipiscing, lacus ultrices</p>
  <h4 style="left:767px">Explore</h4>
  <ul class="links" style="left:769px"><li>Home</li><li>Shop</li><li>About</li><li>Blog</li></ul>
  <ul class="links" style="left:848px"><li>FAQs</li><li>Contact Us</li><li>Price</li><li>testimonials</li></ul>
</footer>
<div class="bottom-bar"><span>Copyright © 2019 Homeopathic</span><div class="cards" aria-label="Accepted payment methods"><i></i><i></i><i></i><i></i><i></i></div></div>

</body>
</html>
```